IT services company needs a business card designed

-2 sided business card.-Front is going to be the logo raised (3D floating effect) on a black background. Make the logos spider web shiny silver and keep the spider the same design. -Back needs to have the following information:Darrel Sotho, Managing Partner, Cell: 738-402-1954, Website: Plankhorn.com, Email: Darrel@Plankhorn.com
Target Market(s)
IT Services
Industry/Entity Type
It Company
Contact Information for Business Card
-2 sided business card.
-Front is going to be the logo raised (3D floating effect) on a black background. Make the logos spider web shiny silver and keep the spider the same design.
-Back needs to have the following information:
Darrel Sotho, Managing Partner, Cell: 738-402-1954, Website: Plankhorn.com, Email: Darrel@Plankhorn.com

```html
<!DOCTYPE html>
<html lang="en">
<head>
<meta charset="utf-8">
<title>Plankhorn Business Card</title>
<link href="https://fonts.googleapis.com/css2?family=Saira:wght@300;400&display=swap" rel="stylesheet">
<style>
  :root {
    --backdrop: #9b9b9b;
    --card-top: #0e0f11;
    --card-bottom: #3b3c3e;
    --accent-blue: #1db4ec;
    --deep-blue: #0e6fa8;
    --silver: #c9cacc;
    --text-light: #e2e2e2;
    --web-grey: #7d7f83;
  }
  html, body {
    margin: 0;
    padding: 0;
    width: 1200px;
    height: 1000px;
    overflow: hidden;
    background: var(--backdrop);
    font-family: "Saira", "Arial", sans-serif;
  }
  .canvas {
    position: relative;
    width: 1200px;
    height: 1000px;
  }
  .card {
    position: absolute;
    top: 212px;
    width: 348px;
    height: 581px;
    background: linear-gradient(180deg, var(--card-top) 0%, var(--card-bottom) 100%);
    overflow: hidden;
  }
  .card-front { left: 219px; }
  .card-back { left: 634px; }

  .brand-mark {
    position: absolute;
    left: 84px;
    top: 150px;
    width: 180px;
    height: 180px;
    border-radius: 50%;
    background: radial-gradient(circle at 50% 50%, var(--accent-blue) 0%, var(--deep-blue) 30%, #6f7175 62%, #b9babd 100%);
  }
  .brand-name {
    position: absolute;
    left: 0;
    right: 0;
    top: 370px;
    margin: 0;
    text-align: center;
    font-weight: 300;
    font-size: 46px;
    letter-spacing: 2px;
    color: var(--silver);
    line-height: 1;
  }

  .web-artwork {
    position: absolute;
    left: 0;
    top: 0;
    width: 300px;
    height: 330px;
    border-bottom-right-radius: 60% 70%;
    border-bottom-left-radius: 10% 20%;
    background:
      radial-gradient(ellipse 90px 130px at 125px 120px, rgba(29,180,236,0.85) 0%, rgba(29,180,236,0.55) 55%, rgba(29,180,236,0) 100%),
      linear-gradient(180deg, rgba(29,180,236,0.35) 0%, rgba(125,127,131,0.45) 55%, rgba(125,127,131,0.3) 100%);
  }

  .holder-name {
    position: absolute;
    left: 40px;
    top: 376px;
    margin: 0;
    font-weight: 400;
    font-size: 24px;
    letter-spacing: 0.5px;
    color: var(--accent-blue);
    line-height: 1;
  }
  .holder-title {
    position: absolute;
    left: 40px;
    top: 404px;
    margin: 0;
    font-weight: 300;
    font-size: 15px;
    color: var(--text-light);
    line-height: 1;
  }
  .contact-list {
    position: absolute;
    left: 40px;
    top: 465px;
    margin: 0;
    padding: 0;
    list-style: none;
  }
  .contact-item {
    display: flex;
    align-items: center;
    height: 27px;
    font-weight: 300;
    font-size: 15px;
    color: var(--text-light);
  }
  .contact-icon {
    width: 14px;
    height: 14px;
    margin-right: 6px;
    fill: none;
    stroke: var(--accent-blue);
    stroke-width: 1.5;
  }
</style>
</head>
<body>
<main class="canvas">
  <section class="card card-front" aria-label="Card front">
    <div class="brand-mark" role="img" aria-label="Company emblem area"></div>
    <h1 class="brand-name">PLANKHORN</h1>
  </section>

  <section class="card card-back" aria-label="Card back">
    <div class="web-artwork" role="img" aria-label="Large blue and silver emblem artwork"></div>
    <h2 class="holder-name">DARREL SOTHO</h2>
    <p class="holder-title">Managing Partner</p>
    <ul class="contact-list">
      <li class="contact-item">
        <svg class="contact-icon" viewBox="0 0 14 14" aria-hidden="true">
          <path d="M3 1.5 L5 4 L4 5.5 C5 7.5 6.5 9 8.5 10 L10 9 L12.5 11 L11 12.8 C6 12.5 1.5 8 1.2 3 Z"/>
        </svg>
        738-402-1954
      </li>
      <li class="contact-item">
        <svg class="contact-icon" viewBox="0 0 14 14" aria-hidden="true">
          <rect x="1" y="3" width="12" height="9"/>
          <path d="M1 3 L7 8 L13 3"/>
        </svg>
        Plankhorn.com
      </li>
      <li class="contact-item">
        <svg class="contact-icon" viewBox="0 0 14 14" aria-hidden="true">
          <circle cx="7" cy="7" r="5.8"/>
          <ellipse cx="7" cy="7" rx="2.6" ry="5.8"/>
          <path d="M1.2 7 H12.8 M2 4 H12 M2 10 H12"/>
        </svg>
        Darrel@Plankhorn.com
      </li>
    </ul>
  </section>
</main>
</body>
</html>
```